Norvane Builders Business Card

Modern and Professional Business Card for a Med size construction/development company.

See the samples below for the design I like … but I need ideas for incorporating the red company logo while still keeping the clean look of the card samples that are attached.

Logo and tag line on the back … info on the front.

Tagline: Quality Starts from the Ground Up

Target Market(s)

Med-Large General Contractors

Contact Information for Business Card

Norvane Builders Limited
42 Brenton Street
Elk Harbour, NL
B3K 7T2

t: 709-555-0147
f: 709-555-0192
w: www.norvanebuilders-example.com

Font styles to use
Sans Serif

Colors
fbee3e

Requirements
Must have
• I like the black and yellow designs of the attached samples …. but I'm not sure how to incorporate the red Norvane Builders logo into that design??
Nice to have
• Construction safety strips

```html
<!DOCTYPE html>
<html lang="en">
<head>
<meta charset="utf-8">
<title>Norvane Builders Business Card</title>
<link rel="stylesheet" href="https://fonts.googleapis.com/css2?family=Arimo:wght@400;700&display=swap">
<style>
  :root {
    --bg: #d9d9d9;
    --red: #e3001b;
    --yellow: #f7f237;
    --gold-light: #f0c733;
    --gold-dark: #d9a51c;
    --white: #ffffff;
  }
  * { box-sizing: border-box; margin: 0; padding: 0; }
  html, body {
    width: 1200px; height: 800px; overflow: hidden;
    background: var(--bg);
    font-family: "Arimo", Arial, sans-serif;
  }
  .canvas {
    width: 1200px; height: 800px;
    display: flex; align-items: center; justify-content: center; gap: 40px;
  }
  .card {
    position: relative;
    width: 540px; height: 310px;
    box-shadow: 0 6px 18px rgba(0,0,0,.25);
  }
  .card__stripe-frame {
    position: absolute; inset: 0;
    background: linear-gradient(135deg, var(--gold-light), var(--gold-dark) 50%, var(--gold-light));
  }
  .card__inner {
    position: absolute; inset: 28px 30px;
    display: flex;
  }
  .panel--red { background: var(--red); }
  .panel--yellow { background: var(--yellow); }

  /* Back */
  .back .panel--side { width: 27%; }
  .back .panel--center {
    width: 46%;
    display: flex; flex-direction: column; align-items: center; justify-content: center;
    text-align: center;
    padding: 0 10px;
  }
  /* Front */
  .front .panel--brand {
    width: 56%;
    display: flex; flex-direction: column; align-items: center; justify-content: center;
  }
  .front .panel--contact {
    width: 44%;
    display: flex; flex-direction: column; justify-content: center; gap: 8px;
    padding-left: 8px; padding-right: 8px;
  }

  .wordmark {
    color: var(--white);
    font-weight: 700;
    text-transform: uppercase;
    line-height: 1.1;
    text-align: center;
  }
  .wordmark__name { display: block; font-size: 34px; letter-spacing: 1px; }
  .wordmark__suffix { display: block; font-size: 14px; letter-spacing: 2px; margin-top: 4px; }
  .back .wordmark__name { font-size: 30px; }
  .back .wordmark__suffix { font-size: 12px; }

  .address {
    margin-top: 16px;
    color: var(--yellow);
    font-size: 11px;
    line-height: 1.4;
    font-style: normal;
  }
  .tagline {
    margin-top: 12px;
    color: var(--white);
    font-size: 11px;
    font-weight: 700;
    letter-spacing: .5px;
    line-height: 1.3;
  }

  .contact-row {
    display: flex; align-items: center; gap: 6px;
    background: var(--red);
    height: 24px;
    padding-left: 4px;
    color: var(--yellow);
    font-size: 13px;
    white-space: nowrap;
  }
  .contact-row--web { font-size: 10.5px; }
  .contact-row__icon { width: 16px; height: 16px; flex: none; }
</style>
</head>
<body>
<main class="canvas">

  <section class="card back" aria-label="Card back">
    <div class="card__stripe-frame" role="img" aria-label="Gold construction safety stripe texture frame"></div>
    <div class="card__inner">
      <div class="panel--yellow panel--side"></div>
      <div class="panel--red panel--center">
        <p class="wordmark"><span class="wordmark__name">Norvane</span><span class="wordmark__suffix">Builders Limited</span></p>
        <address class="address">42 Brenton Street, Elk Harbour<br>NL B3K 7T2</address>
        <p class="tagline">Quality Starts from the Ground Up</p>
      </div>
      <div class="panel--yellow panel--side"></div>
    </div>
  </section>

  <section class="card front" aria-label="Card front">
    <div class="card__stripe-frame" role="img" aria-label="Gold construction safety stripe texture frame"></div>
    <div class="card__inner">
      <div class="panel--red panel--brand">
        <p class="wordmark"><span class="wordmark__name">Norvane</span><span class="wordmark__suffix">Builders Limited</span></p>
      </div>
      <div class="panel--yellow panel--contact">
        <div class="contact-row">
          <svg class="contact-row__icon" viewBox="0 0 16 16" aria-hidden="true">
            <rect width="16" height="16" rx="3" fill="var(--yellow)"/>
            <path d="M4 5c0-1 1-1.5 4-1.5S12 4 12 5v1H10V5H6v1H4z M5 7h6l1 5H4z" fill="var(--red)"/>
          </svg>
          <span>709-555-0147</span>
        </div>
        <div class="contact-row">
          <svg class="contact-row__icon" viewBox="0 0 16 16" aria-hidden="true">
            <rect width="16" height="16" rx="3" fill="var(--yellow)"/>
            <path d="M5 3h6v3H5z M3 7h10v5h-2v-2H5v2H3z M5 11h6v2H5z" fill="var(--red)"/>
          </svg>
          <span>709-555-0192</span>
        </div>
        <div class="contact-row contact-row--web">
          <svg class="contact-row__icon" viewBox="0 0 16 16" aria-hidden="true">
            <rect width="16" height="16" rx="3" fill="var(--yellow)"/>
            <circle cx="8" cy="8" r="5" fill="none" stroke="var(--red)" stroke-width="1.3"/>
            <ellipse cx="8" cy="8" rx="2" ry="5" fill="none" stroke="var(--red)" stroke-width="1"/>
            <path d="M3 8h10" stroke="var(--red)" stroke-width="1"/>
          </svg>
          <span>www.norvanebuilders-example.com</span>
        </div>
      </div>
    </div>
  </section>

</main>
</body>
</html>
```